Endocrinologist needs new stationery

I have a logo from MarkForge and now need stationery with the new logo.

Address: Suite 4, 282 Falcon Street, Richmond, VIC 3121
Phone: 03 9417 2253
Fax: 03 9417 2255
Website: www.drmaylacorwen.com.au
Email: admin@drmaylacorwen.com.au

```html
<!DOCTYPE html>
<html lang="en">
<head>
<meta charset="utf-8">
<title>Dr Mayla Corwen – Stationery</title>
<link rel="stylesheet" href="https://fonts.googleapis.com/css2?family=Poppins:wght@400;500&family=Open+Sans:wght@400&display=swap">
<style>
  :root {
    --bg: #e4e5e7;
    --paper: #ffffff;
    --brand-blue: #2b5e9b;
    --brand-plum: #7b4258;
    --ink: #2c2c2c;
    --ink-soft: #555555;
    --shadow: 0 3px 10px rgba(0,0,0,0.18);
  }
  * { margin: 0; padding: 0; box-sizing: border-box; }
  html, body { width: 1200px; height: 800px; overflow: hidden; }
  body { background: var(--bg); position: relative; font-family: "Poppins", sans-serif; color: var(--ink); }

  .sheet { position: absolute; background: var(--paper); box-shadow: var(--shadow); }
  .brand-name { font-family: "Poppins", sans-serif; font-weight: 500; color: var(--brand-blue); white-space: nowrap; letter-spacing: 0.02em; }

  .contact-block { position: absolute; border-left: 1px solid var(--brand-blue); font-family: "Poppins", sans-serif; color: var(--ink); }
  .contact-block p { white-space: nowrap; display: flex; align-items: center; }
  .contact-block svg { fill: var(--brand-blue); flex: none; }

  /* Letterhead */
  .letterhead { left: 143px; top: 112px; width: 407px; height: 576px; }
  .letterhead .brand-name { position: absolute; left: 38px; top: 51px; font-size: 15px; }
  .letterhead .contact-block { left: 239px; top: 27px; height: 64px; padding-left: 7px; font-size: 7.6px; line-height: 10.2px; }
  .letterhead .contact-block svg { width: 6px; height: 6px; margin-right: 3px; }
  .letterhead .address { margin-bottom: 2px; }
  .recipient { position: absolute; left: 38px; top: 135px; font-family: "Open Sans", sans-serif; color: var(--ink-soft); }
  .recipient .name { font-size: 7.6px; color: var(--ink); margin-bottom: 2px; }
  .recipient p { font-size: 5.6px; line-height: 10px; }
  .letter-body { position: absolute; left: 38px; top: 196px; width: 330px; font-family: "Open Sans", sans-serif; font-size: 5.4px; line-height: 10px; color: var(--ink-soft); text-align: justify; }
  .letter-body p { margin-bottom: 8.5px; }
  .closing { position: absolute; left: 38px; top: 426px; font-family: "Open Sans", sans-serif; color: var(--ink-soft); }
  .closing .sign-off { font-size: 6px; }
  .closing .signature { display: block; width: 46px; height: 16px; margin: 4px 0 3px 6px; background: linear-gradient(90deg, #d9d9d9, #bdbdbd); border-radius: 3px; }
  .closing .signer { font-size: 19px; color: #4a4a4a; }

  /* Business cards */
  .card { top: 113px; width: 211px; height: 121px; border-radius: 7px; }
  .card-front { left: 614px; }
  .card-front .brand-name { position: absolute; left: 0; right: 0; top: 50px; text-align: center; font-size: 16px; }
  .card-back { left: 845px; }
  .card-back .brand-name { position: absolute; left: 13px; top: 56px; font-size: 7.6px; }
  .card-back .contact-block { left: 103px; top: 35px; height: 56px; padding-left: 8px; font-size: 5.4px; line-height: 8.4px; }
  .card-back .contact-block svg { width: 4.4px; height: 4.4px; margin-right: 2px; }
  .card-back .address { margin-bottom: 3px; }

  /* Envelope front */
  .envelope-front { left: 614px; top: 268px; width: 442px; height: 191px; }
  .envelope-front .brand-name { position: absolute; left: 15px; top: 17px; font-size: 15px; }
  .envelope-front .return-address { position: absolute; left: 15px; top: 50px; width: 148px; text-align: center; font-size: 7.4px; line-height: 9.8px; }

  /* Envelope back */
  .envelope-back { left: 613px; top: 493px; width: 444px; height: 195px; }
  .envelope-back .flap { position: absolute; left: 0; top: 0; width: 444px; height: 76px; }
  .envelope-back .brand-name { position: absolute; left: 0; right: 0; top: 20px; text-align: center; font-size: 22px; }
</style>
</head>
<body>

<!-- Letterhead -->
<section class="sheet letterhead">
  <div class="brand-name">Dr Mayla Corwen</div>
  <div class="contact-block">
    <p class="address">Suite 4, 282 Falcon Street,</p>
    <p class="address">Larkfield, VIC 3187</p>
    <p><svg viewBox="0 0 10 10"><path d="M2 1l2 2-1 1.3c.6 1.2 1.5 2.1 2.7 2.7L7 6l2 2-1.2 1.4C4.5 9 1 5.5.6 2.2z"/></svg>03 9417 2253</p>
    <p><svg viewBox="0 0 10 10"><rect x="2" y="0.5" width="6" height="3"/><rect x="0.5" y="3.5" width="9" height="4" rx="1"/><rect x="2" y="7" width="6" height="2.5"/></svg>03 9417 2255</p>
    <p><svg viewBox="0 0 10 10"><path d="M0.5 2h9v6h-9z M0.5 2l4.5 3.5L9.5 2" fill="none" stroke="#2b5e9b" stroke-width="1.2"/></svg>admin@drmaylacorwen.com.au</p>
    <p><svg viewBox="0 0 10 10"><circle cx="5" cy="5" r="4.2" fill="none" stroke="#2b5e9b" stroke-width="1.2"/><path d="M0.8 5h8.4M5 0.8c-2.2 2.5-2.2 5.9 0 8.4M5 0.8c2.2 2.5 2.2 5.9 0 8.4" fill="none" stroke="#2b5e9b" stroke-width="0.8"/></svg>www.drmaylacorwen.com.au</p>
  </div>

  <div class="recipient">
    <p class="name">BELMORA</p>
    <p>Owner</p>
    <p>City/State, Zip Code</p>
  </div>

  <div class="letter-body">
    <p>Lorem ipsum dolor sit amet, consectetur adipiscing elit, sed do eiusmod tempor incididunt ut labore et dolore magna aliqua. Ut enim ad minim veniam, quis nostrud exercitation ullamco laboris nisi ut aliquip ex ea commodo consequat. Duis aute irure dolor in reprehenderit in voluptate velit esse</p>
    <p>commonly used in graphic design, publishing, and web development. It is typically a corrupted version of De finibus bonorum et malorum, a 1st-century BC text by the Roman statesman and philosopher Cicero, with words altered, added, and removed to make it nonsensical and improper Latin. The first two words are the truncation of dolorem ipsum ("pain itself"). Lorem ipsum's purpose is to permit a page layout to be designed, independently of the copy that will subsequently populate it, or to demonstrate various fonts of a typeface without meaningful text that could be distracting.</p>
    <p>At vero eos et accusamus et iusto odio dignissimos ducimus, qui blanditiis praesentium voluptatum deleniti atque corrupti, quos dolores et quas molestias excepturi sint, obcaecati cupiditate non provident, similique sunt in culpa, qui officia deserunt mollitia animi, id est laborum et dolorum fuga. Et harum quidem rerum facilis est et expedita distinctio. Nam libero tempore, cum soluta nobis est eligendi optio, cumque nihil impedit, quo minus id, quod maxime placeat facere possimus, omnis voluptas assumenda est, omnis dolor repellendus. Temporibus autem quibusdam et aut officiis debitis aut rerum necessitatibus saepe eveniet, ut et voluptates repudiandae sint et molestiae non recusandae. Itaque earum rerum hic tenetur a sapiente delectus, ut aut reiciendis voluptatibus maiores alias consequatur aut perferendis doloribus asperiores repellat.</p>
  </div>

  <div class="closing">
    <p class="sign-off">Sincerely,</p>
    <span class="signature" role="img" aria-label="Handwritten signature"></span>
    <p class="signer">Belmora</p>
  </div>
</section>

<!-- Business card front -->
<section class="sheet card card-front">
  <div class="brand-name">Dr Mayla Corwen</div>
</section>

<!-- Business card back -->
<section class="sheet card card-back">
  <div class="brand-name">Dr Mayla Corwen</div>
  <div class="contact-block">
    <p>Suite 4, 282 Falcon Street,</p>
    <p class="address">Larkfield, VIC 3187</p>
    <p><svg viewBox="0 0 10 10"><path d="M2 1l2 2-1 1.3c.6 1.2 1.5 2.1 2.7 2.7L7 6l2 2-1.2 1.4C4.5 9 1 5.5.6 2.2z"/></svg>03 9417 2253</p>
    <p><svg viewBox="0 0 10 10"><rect x="2" y="0.5" width="6" height="3"/><rect x="0.5" y="3.5" width="9" height="4" rx="1"/><rect x="2" y="7" width="6" height="2.5"/></svg>03 9417 2255</p>
    <p><svg viewBox="0 0 10 10"><circle cx="5" cy="5" r="4.2" fill="none" stroke="#2b5e9b" stroke-width="1.2"/><path d="M0.8 5h8.4M5 0.8c-2.2 2.5-2.2 5.9 0 8.4M5 0.8c2.2 2.5 2.2 5.9 0 8.4" fill="none" stroke="#2b5e9b" stroke-width="0.8"/></svg>www.drmaylacorwen.com.au</p>
    <p><svg viewBox="0 0 10 10"><path d="M0.5 2h9v6h-9z M0.5 2l4.5 3.5L9.5 2" fill="none" stroke="#2b5e9b" stroke-width="1.2"/></svg>admin@drmaylacorwen.com.au</p>
  </div>
</section>

<!-- Envelope front -->
<section class="sheet envelope-front">
  <div class="brand-name">Dr Mayla Corwen</div>
  <p class="return-address">Suite 4, 282 Falcon Street,<br>Larkfield, VIC 3187</p>
</section>

<!-- Envelope back -->
<section class="sheet envelope-back">
  <svg class="flap" viewBox="0 0 444 76" aria-hidden="true">
    <path d="M1 0 C8 30 14 68 48 70 L392 70 C426 68 436 30 443 0" fill="#ffffff" stroke="#dedede" stroke-width="1.2"/>
  </svg>
  <div class="brand-name">Dr Mayla Corwen</div>
</section>

</body>
</html>
```